Life Coaching Business - needs business card design with logo

I need a business card and logo design for a life coaching business I started based in Los Angeles. I offer services to clients that wish to bring more balance and overall wholeness to their lives. As of right now, the business name is "Marcus Elwood Coaching." An iidea I had for the logo was to be kind of a Yin-Yang symbol but with dolphins, as the dolphin has symbolic meaning for my business. Although I am really open to other ideas as long as it incorporates the idea of “balance,” “wholeness,” and “dolphins.”I also wanted to incorporate the color blue, maybe in the form of water, waves, or some sort of peaceful imagery.

```html
<!DOCTYPE html>
<html lang="en">
<head>
<meta charset="utf-8">
<title>Marcus Elwood Coaching – Business Card</title>
<link rel="stylesheet" href="https://fonts.googleapis.com/css2?family=Archivo+Black&family=Arimo:wght@400&family=Open+Sans:wght@400&display=swap">
<style>
  :root {
    --page-bg: #eeefef;
    --card-white: #ffffff;
    --brand-teal: #2a93ae;
    --icon-sky: #4dbde3;
    --ink: #141414;
    --label-grey: #7b7d7e;
  }
  * { margin: 0; padding: 0; box-sizing: border-box; }
  html, body { width: 960px; height: 1200px; overflow: hidden; }
  body { background: var(--page-bg); position: relative; font-family: "Arimo", Arial, sans-serif; }

  .sheet-label {
    position: absolute; left: 60px; top: 24px;
    font-family: "Open Sans", sans-serif; font-size: 36px; color: var(--label-grey);
  }

  .card { position: absolute; left: 60px; width: 840px; height: 480px; }
  .card-front { top: 84px; background: var(--card-white); }
  .card-back { top: 636px; background: var(--brand-teal); }

  /* front: brand block */
  .brand-mark {
    position: absolute; left: 189px; top: 165px;
    width: 82px; height: 82px; border-radius: 50%; background: var(--icon-sky);
  }
  .brand-name {
    position: absolute; left: 90px; top: 258px; width: 280px;
    text-align: center; font-family: "Archivo Black", sans-serif;
    color: var(--ink);
  }
  .brand-name-main { display: block; font-size: 25px; line-height: 32px; letter-spacing: 0.3px; }
  .brand-name-sub { display: block; font-size: 13px; line-height: 22px; letter-spacing: 9px; padding-left: 9px; margin-top: 2px; }

  /* front: details */
  .details { position: absolute; left: 427px; top: 126px; color: var(--brand-teal); }
  .details-name {
    font-family: "Archivo Black", sans-serif; font-size: 33px; line-height: 36px; letter-spacing: 0.5px;
  }
  .details-title { font-size: 23px; line-height: 26px; letter-spacing: 0.5px; }
  .details-address { margin-top: 26px; font-size: 17px; line-height: 24px; letter-spacing: 0.4px; }
  .contact-list { list-style: none; margin-top: 7px; }
  .contact-item { display: flex; align-items: center; height: 29px; font-size: 20px; letter-spacing: 0.6px; }
  .contact-icon { width: 21px; height: 21px; margin-right: 26px; flex: none; }

  /* back */
  .back-disc {
    position: absolute; left: 222px; top: 42px; width: 396px; height: 396px;
    border-radius: 50%; background: var(--card-white);
  }
  .back-name {
    position: absolute; left: 222px; top: 192px; width: 396px; text-align: center;
    font-family: "Archivo Black", sans-serif; color: var(--brand-teal);
  }
  .back-name-main { display: block; font-size: 34px; line-height: 44px; letter-spacing: 0.5px; }
  .back-name-sub { display: block; font-size: 18px; line-height: 34px; letter-spacing: 13px; padding-left: 13px; margin-top: 4px; }
</style>
</head>
<body>
  <div class="sheet-label">S-01</div>

  <section class="card card-front">
    <div class="brand-mark" aria-hidden="true"></div>
    <div class="brand-name">
      <span class="brand-name-main">MARCUS ELWOOD</span>
      <span class="brand-name-sub">COACHING</span>
    </div>

    <div class="details">
      <div class="details-name">MARCUS ELWOOD</div>
      <div class="details-title">COACHING</div>
      <div class="details-address">your address here<br>01234</div>
      <ul class="contact-list">
        <li class="contact-item">
          <svg class="contact-icon" viewBox="0 0 20 20" aria-hidden="true">
            <circle cx="10" cy="10" r="10" fill="var(--icon-sky)"/>
            <path d="M7 4.5 L9 6.5 L8 8.5 Q9 11.5 11.5 12.5 L13 11.5 L15 13.5 L13.5 15.5 Q8.5 15 5.5 9 Q5 6 7 4.5Z" fill="#fff"/>
          </svg>000111222
        </li>
        <li class="contact-item">
          <svg class="contact-icon" viewBox="0 0 20 20" aria-hidden="true">
            <circle cx="10" cy="10" r="10" fill="var(--icon-sky)"/>
            <rect x="4.5" y="6" width="11" height="8" fill="none" stroke="#fff" stroke-width="1.4"/>
            <path d="M4.5 6 L10 10.5 L15.5 6" fill="none" stroke="#fff" stroke-width="1.4"/>
          </svg>info@elwoodcoaching.com
        </li>
        <li class="contact-item">
          <svg class="contact-icon" viewBox="0 0 20 20" aria-hidden="true">
            <circle cx="10" cy="10" r="10" fill="var(--icon-sky)"/>
            <path d="M15 5 L5.5 9.5 L9.5 10.5 L10.5 14.5 Z" fill="#fff"/>
          </svg>www.elwoodcoaching.com
        </li>
      </ul>
    </div>
  </section>

  <section class="card card-back">
    <div class="back-disc" aria-hidden="true"></div>
    <div class="back-name">
      <span class="back-name-main">MARCUS ELWOOD</span>
      <span class="back-name-sub">COACHING</span>
    </div>
  </section>
</body>
</html>
```